3 signs to go on a trailer

due to logo change we need to update our trailer design signage the trailer has 3 panels 2 panels @ 650mmx1200 1@500mmx1200, i have attached a sample i was working on please feel free to change anything you feel needs change. im trying to achive a simple and soft design. i also uploaded our new logo in AI file, please feel free to contact me for further information. also a sketch of how the trailer looks like

```html
<!DOCTYPE html>
<html lang="en">
<head>
<meta charset="utf-8">
<title>Verdawash Trailer Signage</title>
<link href="https://fonts.googleapis.com/css2?family=PT+Sans:wght@400;700&display=swap" rel="stylesheet">
<style>
  :root{
    --green-deep:#12773c;
    --green-mid:#1fa54a;
    --green-bright:#6cbf45;
    --green-soft:#85c77a;
    --green-leaf:#59b559;
    --ink:#4d4d4f;
    --grey-panel:#e6e7e8;
    --grey-ring:#c9cacc;
    --white:#ffffff;
    --stage:#ffffff;
  }
  *{box-sizing:border-box;margin:0;padding:0}
  html,body{width:1200px;height:1000px;overflow:hidden;background:var(--stage)}
  body{position:relative;font-family:"PT Sans",Arial,sans-serif}
  .panel{position:absolute;width:230px;height:422px;overflow:hidden;
    box-shadow:0 1px 4px rgba(0,0,0,.35)}
  .panel--grey{background:var(--grey-panel)}
  .panel--white{background:var(--white)}
  .base-band{position:absolute;left:0;bottom:0;width:100%;height:8px}
  .deco-disc{position:absolute;width:106px;height:106px;border-radius:50%;
    background:var(--grey-ring);opacity:.75;right:-2px;bottom:14px}

  /* integrated services panel */
  .photo-strip{position:absolute;left:0;top:127px;width:208px;height:58px}
  .photo-strip::before,.photo-strip::after{content:"";position:absolute;left:0;width:100%;height:3px;background:var(--green-mid)}
  .photo-strip::before{top:0}
  .photo-strip::after{bottom:0;background:var(--green-bright)}
  .photo-strip__image{position:absolute;left:3px;top:8px;width:200px;height:42px;
    background:linear-gradient(90deg,#7d8a86,#b9b4a0 30%,#6f7b80 55%,#a7b2b8 80%,#5c6a7a)}
  .heading{position:absolute;left:9px;font-weight:700;color:var(--ink);font-size:16px;letter-spacing:.2px}
  .heading__rule{display:block;height:3px;margin-top:1px;
    background:linear-gradient(90deg,var(--green-deep),var(--green-bright))}
  .subline{position:absolute;left:7px;font-weight:700;color:var(--ink);font-size:11px}

  /* water blasting panel */
  .hero-photo{position:absolute;left:0;top:0;width:230px;height:202px;
    background:linear-gradient(180deg,#a9aca9 0%,#c8cac6 45%,#8f9aa5 75%,#dcdddd 100%)}

  /* brand */
  .brand{position:absolute;left:0;width:100%;text-align:center}
  .brand__disc{width:62px;height:62px;border-radius:50%;background:var(--green-mid);margin:0 auto 10px}
  .brand__name{font-weight:700;font-size:24px;color:var(--ink);letter-spacing:.5px;line-height:1}
  .brand__url{font-weight:700;font-size:12px;color:var(--green-deep);margin-top:3px}

  .features{position:absolute;left:0;list-style:none}
  .feature{position:relative;height:18px;margin-bottom:10px;color:var(--white);
    font-weight:700;font-size:10.5px;line-height:18px;padding-left:12px;text-transform:uppercase}
  .feature--1{background:var(--green-deep)}
  .feature--2{background:var(--green-bright)}
  .feature--3{background:var(--green-soft)}
  .feature--4{background:var(--green-leaf)}
  .features--pill .feature{width:158px;border-radius:0 9px 9px 0}
  .features--pill .feature__mark{position:absolute;right:2px;top:2px;width:14px;height:14px;border-radius:50%;background:var(--white)}
  .features--tab .feature{width:145px}
  .features--tab .feature__mark{position:absolute;right:-4px;top:4px;width:10px;height:10px;border-radius:50%;background:var(--white);border:2px solid var(--green-mid)}
  .features--step .feature{clip-path:polygon(0 0,calc(100% - 12px) 0,100% 100%,0 100%)}
  .features--step .feature--1{width:130px}
  .features--step .feature--2{width:148px}
  .features--step .feature--3{width:166px}
  .features--step .feature--4{width:193px}
  .feature__mark svg{display:block;width:100%;height:100%}

  .hotline{position:absolute;left:0;width:100%;display:flex;justify-content:center;align-items:center;gap:4px}
  .hotline__icon{width:30px;height:30px}
  .hotline__number{font-weight:700;font-size:18.5px;color:var(--green-deep)}
</style>
</head>
<body>

<svg width="0" height="0" style="position:absolute">
  <defs>
    <symbol id="band" viewBox="0 0 230 8" preserveAspectRatio="none">
      <rect width="230" height="8" fill="#1fa54a"/>
      <polygon points="0,0 24,0 18,8 0,8" fill="#12773c"/>
      <polygon points="24,0 62,0 56,8 18,8" fill="#6cbf45"/>
      <polygon points="62,0 100,0 94,8 56,8" fill="#85c77a"/>
      <polygon points="100,0 138,0 132,8 94,8" fill="#59b559"/>
      <polygon points="138,0 176,0 170,8 132,8" fill="#6cbf45"/>
    </symbol>
    <symbol id="tick" viewBox="0 0 14 14">
      <path d="M3.5 7.2l2.3 2.3 4.7-5" fill="none" stroke="#1fa54a" stroke-width="2" stroke-linecap="round" stroke-linejoin="round"/>
    </symbol>
    <symbol id="phone24" viewBox="0 0 30 30">
      <circle cx="15" cy="15" r="15" fill="#12773c"/>
      <path d="M7.5 9.5c0-1 1-2 2-2l1.5 3-1.3 1.2c.8 2 2.3 3.6 4.3 4.5l1.3-1.3 3 1.5c0 1-1 2-2 2-5 0-8.8-3.9-8.8-8.9z" fill="#fff"/>
      <text x="20" y="15" font-family="PT Sans, Arial, sans-serif" font-weight="700" font-size="8.5" fill="#fff" text-anchor="middle">24</text>
    </symbol>
  </defs>
</svg>

<!-- Panel: integrated services -->
<section class="panel panel--grey" style="left:205px;top:57px">
  <div class="photo-strip">
    <div class="photo-strip__image" role="img" aria-label="Strip of staff photos: cleaning, security and maintenance crews at work"></div>
  </div>
  <h2 class="heading" style="top:216px">INTEGRATED SERVICES<span class="heading__rule" style="width:170px"></span></h2>
  <p class="subline" style="top:238px">Cleaning • Security • Maintenance</p>
  <div class="deco-disc"></div>
  <svg class="base-band"><use href="#band"/></svg>
</section>

<!-- Panel: features with rounded pills -->
<section class="panel panel--white" style="left:498px;top:53px">
  <div class="brand" style="top:60px">
    <div class="brand__disc"></div>
    <div class="brand__name">VERDAWASH</div>
    <div class="brand__url">www.verdawash.com.au</div>
  </div>
  <ul class="features features--pill" style="top:232px">
    <li class="feature feature--1">5800psi pressure<span class="feature__mark"><svg><use href="#tick"/></svg></span></li>
    <li class="feature feature--2">150˚C hot water<span class="feature__mark"><svg><use href="#tick"/></svg></span></li>
    <li class="feature feature--3">No chemicals<span class="feature__mark"><svg><use href="#tick"/></svg></span></li>
    <li class="feature feature--4">100% eco friendly<span class="feature__mark"><svg><use href="#tick"/></svg></span></li>
  </ul>
  <div class="hotline" style="top:362px">
    <svg class="hotline__icon"><use href="#phone24"/></svg>
    <span class="hotline__number">1300 555 019</span>
  </div>
  <svg class="base-band"><use href="#band"/></svg>
</section>

<!-- Panel: water blasting division -->
<section class="panel panel--grey" style="left:755px;top:57px">
  <div class="hero-photo" role="img" aria-label="Photo of an operator in a safety vest water blasting a boat hull"></div>
  <h2 class="heading" style="top:218px">WATER BLASTING DIVISION<span class="heading__rule" style="width:172px"></span></h2>
  <p class="subline" style="top:240px;left:12px;font-size:13px">TN003</p>
  <div class="deco-disc"></div>
  <svg class="base-band"><use href="#band"/></svg>
</section>

<!-- Panel: features with square tabs -->
<section class="panel panel--white" style="left:205px;top:522px">
  <div class="brand" style="top:58px">
    <div class="brand__disc"></div>
    <div class="brand__name">VERDAWASH</div>
    <div class="brand__url">www.verdawash.com.au</div>
  </div>
  <ul class="features features--tab" style="top:231px;left:6px">
    <li class="feature feature--1">5800psi pressure<span class="feature__mark"></span></li>
    <li class="feature feature--2">150˚C hot water<span class="feature__mark"></span></li>
    <li class="feature feature--3">No chemicals<span class="feature__mark"></span></li>
    <li class="feature feature--4">100% eco friendly<span class="feature__mark"></span></li>
  </ul>
  <div class="hotline" style="top:361px">
    <svg class="hotline__icon"><use href="#phone24"/></svg>
    <span class="hotline__number">1300 555 019</span>
  </div>
  <svg class="base-band"><use href="#band"/></svg>
</section>

<!-- Panel: features with stepped bars -->
<section class="panel panel--white" style="left:500px;top:522px">
  <div class="brand" style="top:58px">
    <div class="brand__disc"></div>
    <div class="brand__name">VERDAWASH</div>
    <div class="brand__url">www.verdawash.com.au</div>
  </div>
  <ul class="features features--step" style="top:231px">
    <li class="feature feature--1">5800psi pressure</li>
    <li class="feature feature--2">150˚C hot water</li>
    <li class="feature feature--3">No chemicals</li>
    <li class="feature feature--4">100% eco friendly</li>
  </ul>
  <div class="hotline" style="top:361px">
    <svg class="hotline__icon"><use href="#phone24"/></svg>
    <span class="hotline__number">1300 555 019</span>
  </div>
  <svg class="base-band"><use href="#band"/></svg>
</section>

</body>
</html>
```